We Buy Houses Website

Looking for a highly motivated and skillfull designer to design and code me a "we Buy Houses" type website. I have a potential logo, but if you think you can make a BETTER one, please do try and incorporate it in your template. I am looking for creativity, professionalism, simple yet elegant. I will need a simple form on the front of the template along with pictures I provide you of recent houses I have bought. Look at these sites for examples of the layout of the website:

http://www.brickwaleholdings.example/
http://www.marlowtakesplots.example/
http://www.quickdwellingexit.example/

If you make me a design that blows me away, and you are dependable, you will become part of my team and in charge of the web aspect which will include designing, updating, any and all graphics and logo work, SEO, coding. If you have skills in all of these areas please make me a design and lets do business!! The name of the website will be "Tovin Takes Homes" at TovinTakesHomes.example

I have uploaded some pictures of houses that we have done, please feel free to incorporate this into the banner or the design, etc. I want them to know we buy houses in ANY condition, as is, cash, can close immediately so they can get on with their life. We have many options to help them find a solution to whatever problem they have. We are in the business of helping people.

Target Market(s)

People looking to sell their houses
people facing foreclosure, bankruptcy, death in the family, divorce, anyone that we can help
people with ugly houses that need a lot of repair

Industry/Entity Type

Business

Font styles to use
Serif
Sans Serif

Colors

Designer to choose colors to be used in the design.

Requirements
Must have
• must have a simple form on the front of the page, preferrably near the banner, with the few required fields to help someone get started putting in their interest to sell their house, view the 2 websites i put as examples to see what kind of fields it should have.

My phone number (555) 481-7720 along with a Tovin Takes Homes logo, clean simple and elegant and professional. I want a nice color scheme that is not white but professional and has a wow factor.

```html
<!DOCTYPE html>
<html lang="en">
<head>
<meta charset="utf-8">
<title>Tovin Takes Homes – Sell Your House Fast, For Cash</title>
<link rel="stylesheet" href="https://fonts.googleapis.com/css2?family=Open+Sans:ital,wght@0,400;0,600;0,700;1,600&family=Oswald:wght@400;500&display=swap">
<style>
  :root {
    --navy-deep: #050a1c;
    --navy-bar: #0b1638;
    --navy-ink: #1b3760;
    --lime: #b5e61d;
    --lime-dark: #8fc00e;
    --blue-btn: #0d7de6;
    --blue-btn-dark: #0561c4;
    --red-badge: #d6121b;
    --page-bg: #efefef;
    --panel: #ffffff;
    --panel-line: #e2e2e2;
    --ink: #2a2a2a;
    --ink-soft: #5b5b5b;
    --ink-faint: #d4d4d4;
    --heading-grey: #3f3f3f;
  }
  * { box-sizing: border-box; margin: 0; padding: 0; }
  html, body { width: 867px; height: 1200px; overflow: hidden; }
  body {
    position: relative;
    background: var(--page-bg);
    font-family: "Open Sans", Arial, sans-serif;
    color: var(--ink);
  }
  .abs { position: absolute; }

  /* Header */
  .site-header {
    position: absolute; left: 0; top: 0; width: 867px; height: 92px;
    background: var(--navy-deep);
    border-top: 2px solid var(--lime);
  }
  .brand { position: absolute; left: 103px; top: 40px; display: flex; align-items: center; gap: 7px; }
  .brand-mark { width: 14px; height: 14px; background: var(--lime); }
  .brand-name { font-weight: 700; font-size: 13px; color: var(--lime); letter-spacing: .3px; }
  .header-phone { position: absolute; right: 85px; top: 10px; font-weight: 700; font-size: 13px; color: #fff; }
  .header-email { position: absolute; right: 85px; top: 28px; font-size: 9px; color: #fff; }
  .main-nav { position: absolute; right: 77px; top: 71px; display: flex; gap: 11px; }
  .main-nav a { color: #fff; text-decoration: none; font-size: 9px; font-weight: 600; }

  /* Hero */
  .hero {
    position: absolute; left: 76px; top: 92px; width: 715px; height: 284px;
    background: linear-gradient(180deg, #6d7680 0%, #8d8f8c 35%, #6f6a52 65%, #7a6c45 100%);
  }
  .hero-title { position: absolute; left: 47px; top: 134px; color: #fff; font-weight: 700; font-size: 20px; text-shadow: 0 1px 3px rgba(0,0,0,.6); }
  .hero-sub { position: absolute; left: 54px; top: 163px; color: #fff; font-size: 15px; line-height: 16px; text-shadow: 0 1px 3px rgba(0,0,0,.6); }
  .hero-sub small { font-size: 13px; }
  .btn-blue {
    position: absolute; display: flex; align-items: center; justify-content: center;
    background: linear-gradient(180deg, var(--blue-btn), var(--blue-btn-dark));
    color: #fff; font-size: 11px; font-weight: 600; border-radius: 3px; text-decoration: none;
  }
  .hero .btn-blue { left: 46px; top: 228px; width: 127px; height: 37px; }

  .quote-form {
    position: absolute; left: 453px; top: 13px; width: 217px; height: 261px;
    background: rgba(250,250,250,.94); border-radius: 6px; box-shadow: 0 1px 6px rgba(0,0,0,.4);
  }
  .quote-form h2 { position: absolute; left: 13px; top: 9px; width: 195px; font-size: 12px; font-weight: 400; line-height: 15px; color: #111; }
  .field {
    position: absolute; left: 26px; width: 162px; height: 26px;
    border: 1px solid #e4e4e4; border-radius: 4px; background: #fff;
    font-size: 8px; color: #c2c2c2; padding: 8px 9px;
  }
  .btn-submit {
    position: absolute; left: 47px; top: 214px; width: 128px; height: 38px; border-radius: 3px;
    background: linear-gradient(180deg, #c6f02a, var(--lime-dark));
    color: #fff; font-weight: 700; font-size: 14px; letter-spacing: 1px;
    display: flex; align-items: center; justify-content: center;
  }
  .cash-badge { position: absolute; left: 377px; top: 41px; width: 92px; height: 92px; }

  /* Steps */
  .steps { position: absolute; left: 76px; top: 376px; width: 715px; height: 99px; background: var(--panel); display: flex; }
  .step { flex: 1; position: relative; border-right: 1px solid #eee; }
  .step:last-child { border-right: 0; }
  .step svg { position: absolute; left: 12px; top: 16px; }
  .step h3 { position: absolute; left: 61px; top: 16px; font-family: "Oswald", sans-serif; font-weight: 500; font-size: 13px; line-height: 15px; color: #111; text-transform: uppercase; letter-spacing: -.2px; }
  .step p { position: absolute; left: 61px; top: 51px; width: 112px; font-size: 8px; line-height: 11px; color: var(--ink-soft); }

  /* Panels */
  .panel { position: absolute; background: var(--panel); border: 1px solid var(--panel-line); }
  .map-panel { left: 76px; top: 486px; width: 531px; height: 265px; }
  .map-fill { position: absolute; left: 70px; top: 18px; width: 370px; height: 240px; background: var(--navy-ink); border-radius: 40px 60px 30px 50px; }
  .location-panel { left: 616px; top: 486px; width: 176px; height: 265px; }
  .location-panel h2 { position: absolute; left: 22px; top: 20px; font-family: "Oswald", sans-serif; font-weight: 500; font-size: 26px; line-height: 30px; color: var(--heading-grey); letter-spacing: -1px; }
  .location-panel h2 span { color: var(--navy-ink); }
  .location-panel p { position: absolute; left: 24px; top: 148px; width: 122px; font-size: 8.5px; line-height: 12px; color: var(--ink-faint); font-weight: 600; }

  .projects-panel { left: 76px; top: 762px; width: 531px; height: 131px; }
  .projects-panel h2 { position: absolute; left: 19px; top: 29px; font-family: "Oswald", sans-serif; font-weight: 500; font-size: 18px; line-height: 21px; color: var(--heading-grey); letter-spacing: -.8px; }
  .projects-panel h2 span { color: var(--navy-ink); }
  .arrows { position: absolute; left: 19px; top: 86px; display: flex; gap: 2px; }
  .arrows span { width: 22px; height: 19px; background: #14213d; display: flex; align-items: center; justify-content: center; }
  .project { position: absolute; top: 18px; width: 124px; height: 88px; border: 1px solid #e3e3e3; padding: 7px; background: #fff; }
  .project div { width: 100%; height: 100%; background: linear-gradient(180deg, #3a2a1e 0%, #6b4a30 45%, #a9906f 70%, #8c7a63 100%); }

  .testimonial-panel { left: 616px; top: 762px; width: 176px; height: 251px; }
  .testimonial-panel h2 { position: absolute; left: 22px; top: 21px; font-family: "Oswald", sans-serif; font-weight: 500; font-size: 18px; line-height: 21px; color: var(--heading-grey); letter-spacing: -.8px; }
  .testimonial-panel p { position: absolute; left: 22px; top: 73px; width: 116px; font-size: 8.5px; line-height: 12.2px; color: #444; }
  .testimonial-panel cite { position: absolute; right: 14px; top: 218px; font-size: 8.5px; font-weight: 600; font-style: italic; color: #333; }

  .cta-panel { left: 76px; top: 904px; width: 531px; height: 109px; }
  .cta-panel p { position: absolute; left: 18px; top: 37px; font-size: 14px; line-height: 17px; color: #444; }
  .cta-panel .btn-blue { left: 388px; top: 38px; width: 128px; height: 38px; }

  /* Footer */
  .site-footer { position: absolute; left: 0; top: 1066px; width: 867px; height: 134px; background: var(--navy-deep); border-top: 1px solid #2a2f45; }
  .footer-links { position: absolute; top: 40px; display: grid; row-gap: 2px; }
  .footer-links a { color: #fff; font-size: 8.5px; font-weight: 600; text-decoration: none; line-height: 12px; }
  .social { position: absolute; left: 685px; top: 9px; display: flex; gap: 6px; }
  .social span { width: 24px; height: 24px; border-radius: 50%; background: #3d7fc7; }
  .footer-brand { position: absolute; left: 706px; top: 78px; display: flex; align-items: center; gap: 5px; }
  .footer-brand .brand-mark { width: 10px; height: 10px; }
  .footer-brand .brand-name { font-size: 9px; }
  .copyright-bar { position: absolute; left: 0; bottom: 0; width: 867px; height: 28px; background: var(--navy-bar); }
  .copyright-bar p { position: absolute; right: 78px; top: 9px; font-size: 7px; color: #fff; }
</style>
</head>
<body>

<header class="site-header">
  <div class="brand"><span class="brand-mark"></span><span class="brand-name">Tovin Takes Homes</span></div>
  <div class="header-phone">(555) 481-7720</div>
  <div class="header-email">info@tovintakeshomes.example</div>
  <nav class="main-nav">
    <a href="#">HOME</a><a href="#">WE BUY HOUSES</a><a href="#">HOW IT WORKS</a><a href="#">SERVICES</a><a href="#">TESTIMONIALS</a><a href="#">FAQ</a><a href="#">BLOG</a><a href="#">CONTACT US</a>
  </nav>
</header>

<section class="hero" role="img" aria-label="Photo of a single-storey house with a dry front lawn">
  <h1 class="hero-title">Sell Your House Fast, For Cash</h1>
  <p class="hero-sub">Find a simpler way to sell your home,<br><small>with no fees, no commissions in as-is condition.</small></p>
  <a class="btn-blue" href="#">MORE DETAILS</a>

  <form class="quote-form">
    <h2>We are in the business of helping people</h2>
    <div class="field" style="top:56px">Name</div>
    <div class="field" style="top:92px">Phone</div>
    <div class="field" style="top:128px">Email</div>
    <div class="field" style="top:164px">Property Address</div>
    <div class="btn-submit">SUBMIT</div>
  </form>

  <svg class="cash-badge" viewBox="0 0 92 92" aria-hidden="true">
    <circle cx="46" cy="46" r="45" fill="#f2f2f2"/>
    <circle cx="46" cy="46" r="40" fill="#d6121b"/>
    <text x="49" y="30" fill="#fff" font-family="Open Sans, sans-serif" font-size="13" text-anchor="middle">Get a</text>
    <text x="48" y="47" fill="#fff" font-family="Open Sans, sans-serif" font-size="13" text-anchor="middle">CASH offer</text>
    <text x="48" y="64" fill="#fff" font-family="Open Sans, sans-serif" font-size="13" text-anchor="middle">in 24Hours</text>
  </svg>
</section>

<section class="steps">
  <div class="step">
    <svg width="36" height="40" viewBox="0 0 36 40"><rect x="3" y="2" width="30" height="36" fill="#fff" stroke="#111" stroke-width="2.5"/><path d="M9 11h18M9 17h18M9 23h18M9 29h12" stroke="#111" stroke-width="2"/></svg>
    <h3>Fill in the online<br>form</h3>
    <p>We will always keep your information private.</p>
  </div>
  <div class="step">
    <svg width="36" height="40" viewBox="0 0 36 40"><path d="M8 2l7 9-4 4c2 6 6 11 11 14l4-4 8 7-5 6C14 36 3 20 4 6z" fill="#111"/></svg>
    <h3>Get a call within<br>24 hours</h3>
    <p>A distressed Real Estate expert will call you.</p>
  </div>
  <div class="step">
    <svg width="40" height="40" viewBox="0 0 40 40"><rect x="2" y="4" width="17" height="15" fill="#0f1d3a"/><rect x="21" y="4" width="17" height="15" fill="#0f1d3a"/><rect x="2" y="21" width="17" height="15" fill="#0f1d3a"/><rect x="21" y="21" width="17" height="15" fill="#0f1d3a"/><circle cx="20" cy="11" r="3" fill="#0f1d3a"/><circle cx="11" cy="20" r="3" fill="#0f1d3a"/><circle cx="29" cy="20" r="3" fill="#fff"/></svg>
    <h3>Find a<br>solution</h3>
    <p>We will explore potential solutions.</p>
  </div>
  <div class="step">
    <svg width="38" height="40" viewBox="0 0 38 40"><circle cx="19" cy="20" r="16" fill="none" stroke="#111" stroke-width="2.5"/><text x="19" y="27" font-family="Open Sans, sans-serif" font-size="19" text-anchor="middle" fill="#111">$</text></svg>
    <h3>Go on with<br>your life</h3>
    <p>Focus on rebuilding your future!</p>
  </div>
</section>

<section class="panel map-panel">
  <div class="map-fill" role="img" aria-label="Map of the United States with state borders, in dark blue"></div>
</section>

<section class="panel location-panel">
  <h2>WHERE<br>YOUR<br><span>PROPERTY</span><br>IS LOCATED</h2>
  <p>Lorem ipsum dolor sit amet, consectetur adipisicing elit, sed do eiusmod tempor incididunt ut labore et dolore magna aliqua.</p>
</section>

<section class="panel projects-panel">
  <h2>OUR RECENT<br><span>PROJECTS</span></h2>
  <div class="arrows">
    <span><svg width="10" height="12" viewBox="0 0 10 12"><path d="M8 1L2 6l6 5" fill="none" stroke="#fff" stroke-width="2"/></svg></span>
    <span><svg width="10" height="12" viewBox="0 0 10 12"><path d="M2 1l6 5-6 5" fill="none" stroke="#fff" stroke-width="2"/></svg></span>
  </div>
  <div class="project" style="left:121px"><div role="img" aria-label="Photo of a renovated kitchen with wooden cabinets"></div></div>
  <div class="project" style="left:259px"><div role="img" aria-label="Photo of a renovated kitchen with wooden cabinets"></div></div>
  <div class="project" style="left:397px"><div role="img" aria-label="Photo of a renovated kitchen with wooden cabinets"></div></div>
</section>

<section class="panel testimonial-panel">
  <h2>WHAT CLIENT<br>SAY ABOUT US</h2>
  <p>Sed ut perspiciatis unde omnis iste natus error sit voluptatem accusantium doloremque laudantium, totam rem aperiam, eaque ipsa quae ab illo inventore veritatis et quasi architecto beatae vitae dicta sunt explicabo. Nemo enim ipsam voluptatem quia voluptas sit</p>
  <cite>Orrin Ledger Co.</cite>
</section>

<section class="panel cta-panel">
  <p>We Buy Houses Fast and for Cash<br>Call us at (555) 481-7720 to get a FREE offer today!</p>
  <a class="btn-blue" href="#">CONTACT US</a>
</section>

<footer class="site-footer">
  <nav class="footer-links" style="left:107px"><a href="#">HOME</a><a href="#">WE BUY HOUSES</a><a href="#">HOW IT WORKS</a><a href="#">SERVICES</a></nav>
  <nav class="footer-links" style="left:250px"><a href="#">TESTIMONIALS</a><a href="#">FAQ</a><a href="#">BLOG</a><a href="#">CONTACT US</a></nav>
  <div class="social" aria-label="Social links"><span></span><span></span><span></span></div>
  <div class="footer-brand"><span class="brand-mark"></span><span class="brand-name">Tovin Takes Homes</span></div>
  <div class="copyright-bar"><p>COPYRIGHTS 2014, ALL RIGHTS RESERVED BY TOVIN TAKES HOMES</p></div>
</footer>

</body>
</html>
```